Mapping Bright Currents Through the Modern Seminar Room

This is for a book cover aimed at professors in higher education who want to infuse creative thinking into their classroom. It should have the title on the cover (see name of project). Our first idea is to have a stack of academic type books on a desk in black and white and then have a colorful rainbow light thread hitting the books. However, we are open to options! It has to be sophisticated, cool, and creative ;)

Target Market(s)

Higher Education Instructors

Industry/Entity Type

education

Font styles to use
Serif
Sans Serif

Requirements
Nice to have
• a creative feel of some sort
Should not have
• lightbulbs

```html
<!DOCTYPE html>
<html lang="en">
<head>
<meta charset="utf-8">
<title>Mapping Bright Currents Through the Modern Seminar Room – Cover Wrap</title>
<link rel="stylesheet" href="https://fonts.googleapis.com/css2?family=Oswald:wght@300;500;700&family=Montserrat:wght@400&display=swap">
<style>
  :root{
    --stage:#c4c4c4;
    --space-deep:#07090b;
    --space-mid:#16282a;
    --nebula-teal:#3f8f86;
    --nebula-green:#5fa583;
    --nebula-violet:#6b4a86;
    --glow-warm:#ffd9c4;
    --glow-pink:#f3a7d4;
    --ink-white:#ffffff;
    --ink-black:#0b0b0b;
    --text-soft:#e9e9e9;
    --hue-red:#ec2b2b;
    --hue-orange:#f6861f;
    --hue-yellow:#f7d81a;
    --hue-green:#3cb54a;
    --hue-blue:#2a8fe4;
    --hue-purple:#8148c4;
    --hue-pink:#e83494;
  }
  *{box-sizing:border-box;margin:0;padding:0}
  html,body{width:923px;height:1200px;overflow:hidden}
  body{background:var(--stage);position:relative;font-family:"Montserrat",sans-serif}

  .cover-wrap{
    position:absolute;left:20px;top:337px;width:883px;height:525px;overflow:hidden;
    box-shadow:0 6px 18px rgba(0,0,0,.35);
  }
  .cover-wrap__sky{
    position:absolute;inset:0;
    background:
      radial-gradient(ellipse 200px 140px at 600px 580px, rgba(255,150,60,.35), transparent 70%),
      radial-gradient(ellipse 260px 160px at 590px 420px, var(--glow-warm) 0%, rgba(243,167,212,.55) 25%, transparent 70%),
      radial-gradient(ellipse 300px 170px at 760px 70px, rgba(107,74,134,.6), transparent 70%),
      radial-gradient(ellipse 420px 260px at 640px 150px, var(--nebula-green), transparent 70%),
      radial-gradient(ellipse 300px 200px at 90px 70px, rgba(255,255,255,.25), transparent 70%),
      radial-gradient(ellipse 360px 300px at 330px 220px, var(--space-mid), transparent 80%),
      linear-gradient(180deg, #0d1516 0%, var(--space-deep) 60%, #1b1008 100%);
  }
  .cover-wrap__books{
    position:absolute;left:455px;top:395px;width:285px;height:130px;
    background:linear-gradient(180deg,#f7f1ea 0%,#d9cfc4 30%,#8f6a50 55%,#ece6de 70%,#bfb6aa 100%);
    border-radius:4px 4px 0 0;opacity:.92;
  }

  /* back cover */
  .back-cover{position:absolute;left:0;top:0;width:388px;height:100%}
  .back-cover__title{
    position:absolute;left:56px;top:44px;width:290px;
    font-family:"Oswald",sans-serif;font-weight:700;text-transform:uppercase;
    color:var(--ink-white);font-size:17px;line-height:18px;letter-spacing:.2px;
  }
  .back-cover__blurb{
    position:absolute;left:56px;top:110px;width:270px;
    color:var(--text-soft);font-size:7.4px;line-height:9.15px;text-align:justify;
  }
  .back-cover__blurb p{text-indent:18px}
  .back-cover__note{
    position:absolute;left:56px;top:452px;width:140px;
    color:var(--text-soft);font-size:7.4px;line-height:9.2px;
  }
  .back-cover__code-box{
    position:absolute;left:236px;top:442px;width:88px;height:45px;
    background:var(--ink-white);border-radius:4px;
  }

  /* spine */
  .spine{position:absolute;left:388px;top:0;width:27px;height:100%}
  .spine__title{
    position:absolute;left:50%;top:140px;transform:translateX(-50%) rotate(-90deg) translateX(-50%);
    transform-origin:left top;white-space:nowrap;
    font-family:"Oswald",sans-serif;font-weight:700;text-transform:uppercase;color:var(--ink-white);
    font-size:12px;line-height:11.5px;
  }
  .spine__title{left:4px;top:380px;transform:rotate(-90deg);transform-origin:left top}

  /* front cover */
  .front-cover{position:absolute;left:415px;top:0;width:468px;height:100%}
  .front-cover__title{
    position:absolute;left:100px;top:42px;width:360px;text-align:center;
    font-family:"Oswald",sans-serif;text-transform:uppercase;
  }
  .front-cover__title span{display:block}
  .title-lead{font-weight:700;font-size:64px;line-height:60px;color:var(--ink-white);
    text-shadow:2px 3px 0 rgba(0,0,0,.55);letter-spacing:-1px}
  .title-bright{font-weight:700;font-size:54px;line-height:52px;letter-spacing:-1px;text-shadow:1px 2px 0 rgba(0,0,0,.35)}
  .title-currents{font-weight:700;font-size:46px;line-height:46px;letter-spacing:-1px;text-shadow:1px 2px 0 rgba(0,0,0,.35)}
  .title-link{font-weight:300;font-size:26px;line-height:28px;color:var(--ink-black);letter-spacing:1px}
  .title-heavy{font-weight:700;color:var(--ink-black);letter-spacing:-.5px;
    text-shadow:0 0 2px rgba(255,255,255,.8)}
  .title-heavy--1{font-size:40px;line-height:38px}
  .title-heavy--2{font-size:30px;line-height:29px}
  .title-heavy--3{font-size:24px;line-height:24px;letter-spacing:1px}

  .hue-red{color:var(--hue-red)} .hue-orange{color:var(--hue-orange)}
  .hue-yellow{color:var(--hue-yellow)} .hue-green{color:var(--hue-green)}
  .hue-blue{color:var(--hue-blue)} .hue-purple{color:var(--hue-purple)}
  .hue-pink{color:var(--hue-pink)}
  .front-cover__title .hue{display:inline}
</style>
</head>
<body>
<main class="cover-wrap">
  <div class="cover-wrap__sky" role="img" aria-label="Starry teal and violet nebula sky with a burst of pink and white light rising from an open book"></div>
  <div class="cover-wrap__books" role="img" aria-label="Stack of closed books topped by an open book glowing with light"></div>

  <section class="back-cover">
    <h2 class="back-cover__title">
      Mapping <span class="hue-red">B</span><span class="hue-orange">r</span><span class="hue-yellow">i</span><span class="hue-green">g</span><span class="hue-blue">h</span><span class="hue-purple">t</span> <span class="hue-pink">C</span><span class="hue-red">u</span><span class="hue-orange">r</span><span class="hue-yellow">r</span><span class="hue-green">e</span><span class="hue-blue">n</span><span class="hue-purple">t</span><span class="hue-pink">s</span><br>
      Through the Modern Seminar Room
    </h2>
    <div class="back-cover__blurb">
      <p>Lorem ipsum dolor sit amet, consectetur adipiscing elit, sed do eiusmod tempor incididunt ut labore et dolore magna aliqua. Ut enim ad minim veniam, quis nostrud exercitation ullamco laboris nisi ut aliquip ex ea commodo consequat. Duis aute irure dolor in reprehenderit in voluptate velit esse cillum dolore eu fugiat nulla pariatur. Excepteur sint occaecat cupidatat non proident, sunt in culpa qui officia deserunt mollit anim id est laborum.</p>
      <p>Sed ut perspiciatis unde omnis iste natus error sit voluptatem accusantium doloremque laudantium, totam rem aperiam, eaque ipsa quae ab illo inventore veritatis et quasi architecto beatae vitae dicta sunt explicabo. Nemo enim ipsam voluptatem quia voluptas sit aspernatur aut odit aut fugit, sed quia consequuntur magni dolores eos qui ratione voluptatem sequi nesciunt. Neque porro quisquam est, qui dolorem ipsum quia dolor sit amet, consectetur, adipisci velit, sed quia non numquam eius modi tempora incidunt ut labore et dolore magnam aliquam quaerat voluptatem. Ut enim ad minima veniam, quis nostrum exercitationem ullam corporis suscipit laboriosam, nisi ut aliquid ex ea commodi consequatur? Quis autem vel eum iure reprehenderit qui in ea voluptate velit esse quam nihil molestiae consequatur, vel illum qui dolorem eum fugiat quo voluptas nulla pariatur?</p>
      <p>At vero eos et accusamus et iusto odio dignissimos ducimus qui blanditiis praesentium voluptatum deleniti atque corrupti quos dolores et quas molestias excepturi sint occaecati cupiditate non provident, similique sunt in culpa qui officia deserunt mollitia animi, id est laborum et dolorum fuga. Et harum quidem rerum facilis est et expedita distinctio. Nam libero tempore, cum soluta nobis est eligendi optio cumque nihil impedit quo minus id quod maxime placeat facere possimus, omnis voluptas assumenda est, omnis dolor repellendus. Temporibus autem quibusdam et aut officiis debitis aut rerum necessitatibus saepe eveniet ut et voluptates repudiandae sint et molestiae non recusandae. Itaque earum rerum hic tenetur a sapiente delectus, ut aut reiciendis voluptatibus maiores alias consequatur aut perferendis doloribus asperiores repellat.</p>
    </div>
    <p class="back-cover__note">Lorem ipsum dolor sit amet, consectetur adipiscing elit, sed do eiusmod tempor incididunt ut labore</p>
    <div class="back-cover__code-box"></div>
  </section>

  <section class="spine">
    <h2 class="spine__title">
      Mapping <span class="hue-red">B</span><span class="hue-orange">r</span><span class="hue-yellow">i</span><span class="hue-green">g</span><span class="hue-blue">h</span><span class="hue-purple">t</span> <span class="hue-pink">C</span><span class="hue-red">u</span><span class="hue-orange">r</span><span class="hue-yellow">r</span><span class="hue-green">e</span><span class="hue-blue">n</span><span class="hue-purple">t</span><span class="hue-pink">s</span><br>
      Through the Modern Seminar Room
    </h2>
  </section>

  <section class="front-cover">
    <h1 class="front-cover__title">
      <span class="title-lead">Mapping</span>
      <span class="title-bright"><b class="hue hue-red">B</b><b class="hue hue-orange">R</b><b class="hue hue-yellow">I</b><b class="hue hue-green">G</b><b class="hue hue-blue">H</b><b class="hue hue-purple">T</b></span>
      <span class="title-currents"><b class="hue hue-pink">C</b><b class="hue hue-red">U</b><b class="hue hue-orange">R</b><b class="hue hue-yellow">R</b><b class="hue hue-green">E</b><b class="hue hue-blue">N</b><b class="hue hue-purple">T</b><b class="hue hue-pink">S</b></span>
      <span class="title-link">Through the</span>
      <span class="title-heavy title-heavy--1">Modern</span>
      <span class="title-heavy title-heavy--2">Seminar</span>
      <span class="title-heavy title-heavy--3">Room</span>
    </h1>
  </section>
</main>
</body>
</html>
```